Website for a Psychologist in Private Practice

I need a cool web design for my website: www.drvalporte.com. I would like it to look professional. Keep all the current content and add: Space for video; radio spots (see Silver Harbor Tunes Logo below for those); Quick Inquiry; Chatterbook link; 5 star rating on Rivo; a map; reviews from former patients. I am open to suggestions.

Target Market(s)

Those seeking individual and marital counseling.

Industry/Entity Type

Mental Health

Number of Pages Required

1 page

Font styles to use
Sans Serif
Other font styles liked:
• I'm open but no hard to read script

Requirements
Must have
• All the content on my home page with link for video and radio spots. List services and degrees and expertices (pics not necessary).
Nice to have
• A video of me and radio conversations (logo of Silver Harbor Tunes radio attached).
Should not have
• Cartoons, comedy, etc.... I don't need pictures of services (marital, depression, etc...) Just list those.

```html
<!DOCTYPE html>
<html lang="en">
<head>
<meta charset="utf-8">
<title>Dr. Dana M. Valporte — Psychologist</title>
<link rel="stylesheet" href="https://fonts.googleapis.com/css2?family=Arimo:ital,wght@0,400;0,700;1,400&family=Raleway:wght@400;500;700&display=swap">
<style>
:root{
  --gold:#c6ad4a;
  --gold-band:#cbb457;
  --gold-deep:#9c8a3e;
  --ink:#1d1d1d;
  --text:#555;
  --muted:#8a8a8a;
  --white:#fff;
  --dark-2:#1c1c1c;
}
*{margin:0;padding:0;box-sizing:border-box}
html,body{width:1200px;height:2647px;overflow:hidden}
body{font-family:"Raleway",Arial,sans-serif;color:var(--text);background:var(--white);position:relative}
.body-copy{font-family:"Arimo",Arial,sans-serif}

/* header */
.site-header{position:absolute;left:0;top:0;width:1200px;height:83px;background:var(--white)}
.brand{position:absolute;left:78px;top:16px;font-size:40px;font-weight:500;color:var(--gold);letter-spacing:.5px}
.nav a{position:absolute;top:25px;height:33px;line-height:33px;font-family:"Arimo",Arial,sans-serif;font-size:14.5px;color:var(--ink);text-decoration:none;letter-spacing:.3px}
.nav a.is-active{background:var(--gold);color:var(--white);padding:0 11px}

/* hero */
.hero{position:absolute;left:0;top:83px;width:1200px;height:595px;
  background:
    radial-gradient(ellipse 260px 200px at 840px 390px,rgba(150,120,85,.45),rgba(150,120,85,0) 70%),
    radial-gradient(ellipse 300px 160px at 900px 240px,rgba(200,185,165,.55),rgba(200,185,165,0) 70%),
    linear-gradient(180deg,rgba(255,255,255,0) 60%,rgba(190,175,155,.55) 100%),
    linear-gradient(100deg,#f7f4ee 0%,#efe9df 40%,#e4dbcc 62%,#f1ece3 82%,#d3c6b1 100%)}
.hero-title{position:absolute;left:80px;top:140px;font-size:60px;line-height:72px;font-weight:400;color:var(--ink)}
.hero-title strong{color:var(--gold);font-weight:700}
.btn-solid{position:absolute;left:78px;top:393px;width:270px;height:51px;background:var(--gold);color:var(--white);font-family:"Arimo",Arial,sans-serif;font-size:18px;line-height:51px;text-align:center;letter-spacing:.5px}

/* services */
.services{position:absolute;left:0;top:678px;width:1200px;height:312px;background:linear-gradient(180deg,var(--gold-band),#c7b04e)}
.service{position:absolute;top:0;height:312px;color:var(--white);text-align:center}
.service h3{font-size:23px;font-weight:400;line-height:29px}
.service p{font-family:"Arimo",Arial,sans-serif;font-size:15.5px;line-height:23px;margin-top:18px}
.service--featured{left:432px;width:332px;background:var(--gold-deep)}
.service--featured .frame{position:absolute;left:11px;top:11px;width:310px;height:290px;border:2px solid rgba(255,255,255,.75)}
.btn-line{display:inline-block;border:2px solid var(--white);color:var(--white);font-family:"Arimo",Arial,sans-serif;font-size:18px;width:146px;height:52px;line-height:48px;text-align:center}

/* about */
.section-title{position:absolute;left:0;width:1200px;text-align:center;font-size:42px;font-weight:400;color:var(--ink)}
.section-title span{color:var(--gold)}
.about-text{position:absolute;left:78px;top:1112px;width:585px;font-size:15px;line-height:23px;color:var(--text)}
.btn-outline{position:absolute;left:78px;top:1324px;width:155px;height:51px;border:2px solid var(--gold);color:var(--gold);font-family:"Arimo",Arial,sans-serif;font-size:18px;line-height:47px;text-align:center}
.video{position:absolute;left:727px;top:1115px;width:395px;height:260px;background:radial-gradient(circle at 50% 45%,#7a7260,#34402f 70%,#1f2a20)}
.video svg{position:absolute;left:167px;top:100px}

/* testimonial */
.testimonial{position:absolute;left:0;top:1428px;width:1200px;height:333px;background:linear-gradient(180deg,#4b4a47,#3b3835 60%,#2f2a25)}
.testimonial h2{position:absolute;top:42px;width:1200px;text-align:center;font-size:42px;font-weight:400;color:var(--gold)}
.testimonial blockquote{position:absolute;left:238px;top:120px;width:724px;text-align:center;color:var(--white);font-size:15.5px;line-height:23px}
.testimonial .quote-mark{position:absolute;left:176px;top:106px}
.testimonial cite{position:absolute;top:212px;width:1200px;text-align:center;font-style:normal;color:var(--white);font-size:21px}
.testimonial cite small{display:block;font-family:"Arimo",Arial,sans-serif;font-size:14px;font-style:italic;margin-top:1px}
.dots{position:absolute;top:1707px;left:568px;display:flex;gap:10px}
.dots i{width:11px;height:11px;border-radius:50%;border:2px solid var(--white)}
.dots i.on{background:var(--gold);border-color:var(--gold)}

/* donations */
.partner-badge{position:absolute;width:187px;height:115px;background:#ececec}
.partner-text{position:absolute;width:285px;font-size:15px;line-height:23px;color:var(--muted)}
.partner-text h4{font-size:18px;font-weight:700;color:var(--ink);white-space:nowrap;margin-bottom:3px;line-height:24px}

/* contact */
.contact{position:absolute;left:0;top:2063px;width:1200px;height:584px;background:linear-gradient(180deg,#2e2e2e,var(--dark-2))}
.contact h2{position:absolute;top:46px;width:1200px;text-align:center;font-size:42px;font-weight:400;color:var(--white)}
.contact h2 span{color:var(--gold)}
.contact .intro{position:absolute;left:280px;top:110px;width:640px;text-align:center;color:var(--white);font-size:15.5px;line-height:24px}
.field{position:absolute;background:var(--white);color:#aaa;font-family:"Arimo",Arial,sans-serif;font-size:15px;padding:16px 18px}
.btn-submit{position:absolute;left:579px;top:428px;width:157px;height:51px;border:2px solid var(--gold);color:var(--gold);font-family:"Arimo",Arial,sans-serif;font-size:18px;line-height:47px;text-align:center}
.info{position:absolute;left:820px;color:var(--white);font-family:"Arimo",Arial,sans-serif;font-size:14.5px;line-height:24px}
.info svg{position:absolute;left:0}
.info div{margin-left:55px}
.info .name{font-family:"Raleway",Arial,sans-serif;color:var(--gold);font-size:20px;line-height:30px}
.social{position:absolute;left:819px;top:428px;display:flex;gap:12px}
.social span{height:51px;padding:0 9px;border:2px solid #666;color:#bbb;font-family:"Arimo",Arial,sans-serif;font-size:12.5px;line-height:47px}
.social span.on{border-color:var(--gold);color:var(--gold)}
.footer-rule{position:absolute;left:78px;top:531px;width:1044px;height:1px;background:#555}
.copyright{position:absolute;top:548px;width:1200px;text-align:center;color:#ddd;font-size:14px}
.copyright span{color:var(--gold)}
</style>
</head>
<body>

<header class="site-header">
  <div class="brand">Dr. Dana M. Valporte</div>
  <nav class="nav">
    <a class="is-active" style="left:626px">HOME</a>
    <a style="left:723px">SESSIONS</a>
    <a style="left:842px">RESOURCES</a>
    <a style="left:979px">BIO</a>
    <a style="left:1045px">CONTACT</a>
  </nav>
</header>

<section class="hero" role="img" aria-label="Bright living room with sheer white curtains and a soft rug, a woman reading with a cup of tea in a rattan chair">
  <h1 class="hero-title">I Look Forward to<br><strong>Working</strong> with<br>YOU</h1>
  <div class="btn-solid">MAKE AN APPOINTMENT</div>
</section>

<section class="services">
  <div class="service" style="left:0;width:432px;padding-top:84px">
    <h3>Dating &amp; Marriage</h3>
    <p style="margin-top:40px">Lorem Ipsum is simply dummy text of the<br>printing and typesetting industry. Lorem<br>Ipsum has been.</p>
  </div>
  <div class="service service--featured">
    <div class="frame"></div>
    <div style="position:relative;padding-top:38px">
      <h3>Parenting &amp; Professional<br>Relationships</h3>
      <p>Lorem Ipsum is simply dummy text of<br>the printing and typesetting industry.<br>Lorem Ipsum has been.</p>
      <div style="margin-top:24px"><span class="btn-line">VIEW ALL</span></div>
    </div>
  </div>
  <div class="service" style="left:764px;width:436px;padding-top:84px">
    <h3>Depresssions &amp; Anxiety<br>Issues</h3>
    <p style="margin-top:11px">Lorem Ipsum is simply dummy text of the<br>printing and typesetting industry. Lorem<br>Ipsum has been.</p>
  </div>
</section>

<h2 class="section-title" style="top:1035px">About <span>Dr. Dana M. Valporte</span></h2>
<p class="about-text body-copy">I'm so glad you are here.&nbsp; Choosing to see a professional for issues in your life<br>can be difficult but also possibly life changing.&nbsp; Many postpone seeking help<br>because they believe doing so acknowledges failure on their part.&nbsp; Reallly?&nbsp; We<br>seek the help of experts all the time (contractors, mechanics, chefs, etc...) and<br>what is more important than your life? Consulting with a neutral party to act in your<br>best interest can be time well spent.&nbsp; So if you are willing to take the time to invest<br>in counseling, make sure that it is with someone that is worth your time.</p>
<div class="btn-outline">READ MORE</div>
<div class="video" role="img" aria-label="Introduction video of the therapist outdoors">
  <svg width="62" height="62" viewBox="0 0 62 62"><circle cx="31" cy="31" r="29" fill="none" stroke="#fff" stroke-width="2.5"/><path d="M25 19 L44 31 L25 43 Z" fill="#fff"/></svg>
</div>

<section class="testimonial" role="img" aria-label="Dim photo of a man stretching his arms open against a city skyline">
  <h2>Therapist</h2>
  <svg class="quote-mark" width="38" height="30" viewBox="0 0 38 30"><path d="M2 30V16C2 7 7 2 15 1v6c-4 1-6 4-6 8h6v15zM22 30V16c0-9 5-14 13-15v6c-4 1-6 4-6 8h6v15z" fill="#fff"/></svg>
  <blockquote class="body-copy">Lorem Ipsum is simply dummy text of the printing and typesetting industry. Lorem Ipsum has been the<br>industry's standard dummy text ever since the 1500s, when an unknown printer took a galley of type<br>and scrambled it to make a type specimen book.</blockquote>
  <cite>- Mark Ellison<small>CEO, Northfield Group</small></cite>
</section>
<div class="dots"><i class="on"></i><i></i><i></i></div>

<h2 class="section-title" style="top:1807px">A Portion of all Revenue is <span>Donated</span> to</h2>
<div class="partner-badge" style="left:78px;top:1897px" role="img" aria-label="Partner charity badge"><svg width="187" height="115"><rect x="30" y="33" width="127" height="49" rx="6" fill="#d7d7d7"/></svg></div>
<div class="partner-text body-copy" style="left:282px;top:1893px"><h4>Lorem ipsum is simply dummy</h4>Lorem Ipsum is simply dummy text of<br>the printing and typesetting industry.<br>Lorem Ipsum has been the industry's<br>standard dummy text ever since the.</div>
<div class="partner-badge" style="left:623px;top:1897px" role="img" aria-label="Partner charity badge"><svg width="187" height="115"><rect x="30" y="33" width="127" height="49" rx="6" fill="#d7d7d7"/></svg></div>
<div class="partner-text body-copy" style="left:828px;top:1893px"><h4>Lorem ipsum is simply dummy</h4>Lorem Ipsum is simply dummy text of<br>the printing and typesetting industry.<br>Lorem Ipsum has been the industry's<br>standard dummy text ever since the.</div>

<section class="contact" aria-label="Contact">
  <h2><span>Contact</span> Us Now</h2>
  <p class="intro body-copy">Lorem Ipsum is simply dummy text of the printing and typesetting industry. Lorem Ipsum<br>has been the industry's standard dummy text.</p>
  <div class="field" style="left:78px;top:182px;width:322px;height:51px">Your Name</div>
  <div class="field" style="left:411px;top:182px;width:325px;height:51px">Your E-Mail</div>
  <div class="field" style="left:78px;top:244px;width:322px;height:51px">Your Phone</div>
  <div class="field" style="left:411px;top:244px;width:325px;height:51px">Subject</div>
  <div class="field" style="left:78px;top:307px;width:658px;height:104px">Message</div>
  <div class="btn-submit">SUBMIT</div>

  <div class="info" style="top:188px">
    <svg width="30" height="40" viewBox="0 0 30 40" style="top:14px"><path d="M15 2C8 2 3 7 3 14c0 9 12 23 12 23s12-14 12-23C27 7 22 2 15 2z" fill="none" stroke="#fff" stroke-width="2"/><circle cx="15" cy="14" r="4.5" fill="none" stroke="#fff" stroke-width="2"/></svg>
    <div><span class="name">Dr. Dana M. Valporte</span><br>414 Larkspur Avenue, Suite 120<br>Harbor Point, CA 92001</div>
  </div>
  <div class="info" style="top:300px">
    <svg width="32" height="32" viewBox="0 0 32 32" style="top:-4px"><path d="M8 3l5 6-3 4c2 4 5 7 9 9l4-3 6 5-3 5C15 29 3 17 3 6z" fill="none" stroke="#fff" stroke-width="2" stroke-linejoin="round"/></svg>
    <div>(555) 210 4837</div>
  </div>
  <div class="info" style="top:361px">
    <svg width="32" height="24" viewBox="0 0 32 24" style="top:1px"><rect x="2" y="2" width="28" height="20" fill="none" stroke="#fff" stroke-width="2"/><path d="M2 2l14 11L30 2M2 22l10-9M30 22l-10-9" fill="none" stroke="#fff" stroke-width="2"/></svg>
    <div>dv@drvalporte.com</div>
  </div>
  <div class="social"><span class="on">Chatterbook</span><span>Chirper</span><span>Linkroll</span></div>

  <div class="footer-rule"></div>
  <p class="copyright">© <span>drvalporte</span> - 2016. All Rights Reserved.</p>
</section>

</body>
</html>
```